Design a double sided business card

We are looking for a clean, eye-catching, and contemporary design that enhances the brand and presents a premium, professional image. Our preference is for a brown card with black gloss detailing and embossed elements; however, we are open to creative input and design suggestions that best achieve a strong visual impact.

Please see the attached existing business card for reference. We use both black and brown colours consistently across our branding.

On sample provided

```html
<!DOCTYPE html>
<html lang="en">
<head>
<meta charset="utf-8">
<title>Stratum – Business Card</title>
<link rel="stylesheet" href="https://fonts.googleapis.com/css2?family=Montserrat:wght@400;500;700&display=swap">
<style>
  :root {
    --backdrop: #141414;
    --card: #1e1e1e;
    --gold: #c9b190;
    --gold-soft: #bfa888;
  }
  * { margin: 0; padding: 0; box-sizing: border-box; }
  html, body {
    width: 1200px; height: 1059px; overflow: hidden;
    background: var(--backdrop);
    font-family: "Montserrat", sans-serif;
    color: var(--gold);
  }
  .canvas { position: relative; width: 1200px; height: 1059px; }
  .card {
    position: absolute; left: 255px; width: 690px; height: 392px;
    background: var(--card); border-radius: 16px;
  }
  .card--front { top: 89px; }
  .card--back { top: 547px; }

  .brand-name {
    font-family: "Montserrat", sans-serif;
    font-weight: 700; letter-spacing: 0.12em; color: var(--gold);
    line-height: 1;
  }
  .card--front .brand-name { position: absolute; left: 42px; top: 53px; font-size: 34px; }

  .holder { position: absolute; left: 42px; top: 140px; }
  .holder__name { font-weight: 700; font-size: 23px; line-height: 1; letter-spacing: 0.01em; }
  .holder__role { font-weight: 400; font-size: 15px; margin-top: 4px; }

  .address { position: absolute; left: 42px; top: 203px; font-size: 15px; line-height: 22px; }

  .contacts { position: absolute; left: 42px; top: 264px; list-style: none; font-size: 15px; }
  .contacts li { display: flex; align-items: center; height: 24px; }
  .contacts svg { width: 12px; height: 12px; margin-right: 8px; fill: var(--gold); flex: none; }

  .feature-block {
    position: absolute; left: 388px; top: 54px; width: 272px; height: 284px;
    border: 14px solid var(--gold-soft);
  }

  .back-mark {
    position: absolute; left: 290px; top: 119px; width: 110px; height: 98px;
    border: 6px solid var(--gold);
  }
  .card--back .brand-name {
    position: absolute; left: 0; right: 0; top: 236px;
    text-align: center; font-size: 44px;
  }
  .back-url {
    position: absolute; left: 0; right: 0; top: 338px;
    text-align: center; font-size: 15px; font-weight: 500; letter-spacing: 0.2em;
  }
</style>
</head>
<body>
<main class="canvas">
  <section class="card card--front">
    <div class="brand-name">STRATUM</div>
    <div class="holder">
      <p class="holder__name">DEV ARORA</p>
      <p class="holder__role">Director</p>
    </div>
    <address class="address" style="font-style:normal">
      12 Orchard Mews Lane<br>
      Eastbrook EB4 2LM
    </address>
    <ul class="contacts">
      <li>
        <svg viewBox="0 0 24 24" aria-hidden="true"><path d="M6.6 10.8c1.4 2.8 3.8 5.1 6.6 6.6l2.2-2.2c.3-.3.7-.4 1-.2 1.1.4 2.3.6 3.6.6.6 0 1 .4 1 1V20c0 .6-.4 1-1 1C10.6 21 3 13.4 3 4c0-.6.4-1 1-1h3.5c.6 0 1 .4 1 1 0 1.3.2 2.5.6 3.6.1.3 0 .7-.2 1z"/></svg>
        0800 555 0142
      </li>
      <li>
        <svg viewBox="0 0 24 24" aria-hidden="true"><path d="M7 1h10a2 2 0 0 1 2 2v18a2 2 0 0 1-2 2H7a2 2 0 0 1-2-2V3a2 2 0 0 1 2-2zm0 3v14h10V4zm5 15.2a1.2 1.2 0 1 0 0 2.4 1.2 1.2 0 0 0 0-2.4z"/></svg>
        07700900461
      </li>
      <li>
        <svg viewBox="0 0 24 24" aria-hidden="true"><path d="M2 5h20v14H2zm2 2v.4l8 5.2 8-5.2V7zm0 2.8V17h16V9.8l-8 5.2z"/></svg>
        dev@stratum.co.uk
      </li>
      <li>
        <svg viewBox="0 0 24 24" aria-hidden="true"><path d="M12 2a10 10 0 1 0 0 20 10 10 0 0 0 0-20zm6.9 6h-3a15 15 0 0 0-1.3-3.8A8 8 0 0 1 18.9 8zM12 4c.8 1.1 1.5 2.5 1.9 4h-3.8c.4-1.5 1.1-2.9 1.9-4zM4.3 14a8 8 0 0 1 0-4h3.4a16 16 0 0 0 0 4zm.8 2h3a15 15 0 0 0 1.3 3.8A8 8 0 0 1 5.1 16zm3-8h-3a8 8 0 0 1 4.3-3.8A15 15 0 0 0 8.1 8zM12 20c-.8-1.1-1.5-2.5-1.9-4h3.8c-.4 1.5-1.1 2.9-1.9 4zm2.3-6H9.7a14 14 0 0 1 0-4h4.6a14 14 0 0 1 0 4zm.3 5.8a15 15 0 0 0 1.3-3.8h3a8 8 0 0 1-4.3 3.8zM16.3 14a16 16 0 0 0 0-4h3.4a8 8 0 0 1 0 4z"/></svg>
        www.stratum.co.uk
      </li>
    </ul>
    <div class="feature-block" aria-hidden="true"></div>
  </section>

  <section class="card card--back">
    <div class="back-mark" aria-hidden="true"></div>
    <div class="brand-name">STRATUM</div>
    <p class="back-url">WWW.STRATUM.CO.UK</p>
  </section>
</main>
</body>
</html>
```